Quillbase Design Project - App Review

Take a look at this website, gridvault.example. We are creating something very similar to this, four pages are required. The name of our website is BrightPickDigest.example
1) The home page which highlights, app of the day, a carousel which highlights featured apps, and top apps in different categories
2) Single App Page - This page will details the app that is selected, app icon, app description, app ratings, and other information you can find on an app page in the lumora market
3) A page that list all the apps in a category, for example if the user select, "100 top apps" the page that will display the list of 100 apps, 10 per page, summary of description, a small icon, screenshot etc for each app
4) Review Page - where we review an app of the day, including screenshots, videos, text reviews etc
I do not have any logo at the moment, use these as nav links; home, my apps, reviews, blog and contact. Thank you.
I will like to see a nice creativity. I am open to a very beautiful color combinations. Thank you
Target Market(s)
App shoppers, people that are looking for new apps, discounted apps etc
Industry/Entity Type
Store
Look and feel

```html
<!DOCTYPE html>
<html lang="en">
<head>
<meta charset="utf-8">
<title>BrightPickDigest – Home</title>
<link href="https://fonts.googleapis.com/css2?family=Arimo:wght@400;700&family=Sorts+Mill+Goudy&display=swap" rel="stylesheet">
<style>
:root{
  --ink:#333;
  --muted:#777;
  --topbar:#2e2e2e;
  --header:#d84f2d;
  --orange:#e0522d;
  --gold:#e39a3b;
  --amber:#e48a2a;
  --line:#d6d6d6;
  --footer:#333;
  --white:#fff;
}
*{box-sizing:border-box;margin:0;padding:0}
html,body{width:1200px;height:1066px;overflow:hidden}
body{position:relative;font-family:"Arimo",Arial,sans-serif;color:var(--ink);
  background:radial-gradient(ellipse at 50% 45%,#fff 0%,#f7f7f7 55%,#ececec 100%)}
a{color:inherit;text-decoration:none}
.abs{position:absolute}

/* top bar */
.topbar{left:0;top:0;width:1200px;height:30px;background:var(--topbar)}
.catnav{left:199px;top:9px;font-size:10px;color:#eee;letter-spacing:.2px;white-space:nowrap}
.catnav span{margin:0 6px;color:#aaa}
.catselect{left:869px;top:6px;width:132px;height:18px;background:linear-gradient(#fafafa,#ddd);border:1px solid #bbb;font-size:8px;color:#555;padding:4px 6px}
.catselect svg{position:absolute;right:5px;top:6px}

/* header */
.header{left:0;top:30px;width:1200px;height:112px;background:var(--header)}
.account{right:199px;top:44px;font-size:12px;color:var(--white)}
.account span{margin:0 5px}
.brand{left:200px;top:72px;font-size:30px;color:var(--white);letter-spacing:-.5px}
.mainnav{left:583px;top:79px;width:419px;height:30px;background:var(--white);border-radius:6px;display:flex;overflow:hidden;box-shadow:0 6px 8px -4px rgba(0,0,0,.25)}
.mainnav a{height:30px;line-height:30px;font-size:13px;color:#999;text-align:center;border-left:1px dashed #bbb}
.mainnav a:first-child{border-left:0;color:var(--orange);background:linear-gradient(90deg,#e19a3e 0,#fff 16px);border-radius:6px 0 0 6px}

/* search */
.search{left:381px;top:157px;width:438px;height:45px;background:var(--white);border:1px solid #bbb;border-radius:2px;box-shadow:0 8px 10px -8px rgba(0,0,0,.25)}
.search .ph{position:absolute;left:9px;top:16px;font-size:11px;color:#aaa}
.search .sep{position:absolute;left:389px;top:7px;width:1px;height:31px;background:#ccc}
.search svg{position:absolute;left:397px;top:7px}

/* headings */
.h-serif{font-family:"Sorts Mill Goudy",Georgia,serif;font-size:35px;font-weight:400}
.h-day{left:200px;top:224px;color:var(--orange)}
.h-top{left:745px;top:224px;color:var(--gold)}
.h-feat{left:200px;top:656px;color:#333}
.vdiv{left:727px;top:232px;width:1px;height:378px;background:var(--line)}

/* app of day */
.app{left:200px;width:511px;height:90px}
.app .icon{position:absolute;left:0;top:0;width:50px;height:48px;border:1px solid #999}
.app h3{position:absolute;left:57px;top:-2px;font-size:14px;font-weight:400;color:#222}
.app .meta{position:absolute;left:57px;top:17px;font-size:10px;color:#444;white-space:nowrap}
.app .desc{position:absolute;left:57px;top:34px;width:400px;font-size:9.2px;line-height:11.6px;color:#777;letter-spacing:.15px}
.app .price{position:absolute;left:458px;top:0;width:53px;height:49px;color:var(--white);text-align:center}
.price.paid{background:var(--orange)}
.price.free{background:var(--gold)}
.price b{display:block;font-weight:400;font-size:19px;margin-top:6px}
.price small{display:block;font-size:9.5px;margin-top:2px}
.app .checks{position:absolute;left:460px;top:52px;font-size:9.5px;color:#555;line-height:15.5px}
.checks i{display:inline-block;width:10px;height:10px;border:1px solid #999;vertical-align:-1px;margin-right:8px;background:#fff}
.checks i.hl{border-color:var(--gold)}
.hsep{left:200px;width:511px;height:1px;background:var(--line)}

/* top apps */
.topbox{left:744px;top:279px;width:257px;height:331px;background:var(--white);border:1px solid #ddd}
.topbox .row{position:absolute;left:0;width:255px;font-size:11.2px;color:var(--amber);padding-left:18px}
.topbox .row:before{content:"";position:absolute;left:7px;top:3px;border-left:6px solid var(--amber);border-top:3.5px solid transparent;border-bottom:3.5px solid transparent}
.topbox .row.open:before{left:6px;top:4px;border-top:6px solid var(--amber);border-left:3.5px solid transparent;border-right:3.5px solid transparent;border-bottom:0}
.topbox .sub{position:absolute;left:19px;top:24px;font-size:9.2px;line-height:12px;color:#888}
.topbox .rule{position:absolute;left:0;width:255px;height:1px;background:#e2e2e2}
.viewmore{left:935px;top:580px;width:58px;height:22px;background:var(--gold);color:var(--white);font-size:10px;text-align:center;line-height:22px;border-bottom:2px solid #b9772a}

/* featured */
.longrule{left:200px;top:633px;width:801px;height:2px;background:linear-gradient(90deg,transparent,#999 10%,#999 90%,transparent)}
.featrule{left:425px;top:681px;width:529px;height:1px;background:#bbb}
.arrow{top:672px;width:17px;height:17px;background:var(--orange)}
.card{top:712px;width:180px;text-align:center}
.card .shot{width:106px;height:108px;margin:0 auto;border:2px solid #666}
.card h4{font-size:13.4px;font-weight:400;color:#222;margin-top:6px}
.card p{font-size:9.2px;line-height:11.8px;color:#555;margin-top:3px;letter-spacing:.2px}
.card .btn{display:inline-block;margin-top:8px;width:58px;height:22px;line-height:20px;background:var(--orange);color:var(--white);font-size:10.4px;border-bottom:2px solid #a8351b}
.cdiv{top:728px;width:1px;height:160px;background:linear-gradient(transparent,#ccc 20%,#ccc 80%,transparent)}
.endrule{left:200px;top:930px;width:801px;height:1px;background:#bbb}

/* footer */
.footer{left:0;top:984px;width:1200px;height:82px;background:var(--footer)}
.fnav{left:200px;top:1004px;font-size:12px;color:#ccc}
.fnav span{margin:0 11px;color:#999}
.copy{left:200px;top:1032px;font-size:9.4px;color:#aaa}
.social{top:1013px;width:24px;height:24px;border-radius:50%;background:#e8e8e8;border:1px solid #999}
</style>
</head>
<body>

<div class="abs topbar"></div>
<nav class="abs catnav">MOBILE<span>|</span>DESKTOP<span>|</span>PHONE<span>|</span>TABLET<span>|</span>UNIVERSAL<span>|</span>PAID<span>|</span>FREE<span>|</span>POPULAR<span>|</span>NEW<span>|</span>PRICE DROPS<span>|</span>UPDATES<span>|</span>ALL</nav>
<div class="abs catselect">All Categories<svg width="9" height="5"><path d="M0 0h9L4.5 5z" fill="#777"/></svg></div>

<header class="abs header"></header>
<div class="abs account"><a href="#">Login</a><span>|</span><a href="#">Register</a></div>
<div class="abs brand">BrightPickDigest</div>
<nav class="abs mainnav">
  <a href="#" style="width:75px">Home</a>
  <a href="#" style="width:86px">My Apps</a>
  <a href="#" style="width:87px">Reviews</a>
  <a href="#" style="width:69px">Blog</a>
  <a href="#" style="width:102px">Contact Us</a>
</nav>

<div class="abs search">
  <span class="ph">Search...</span><span class="sep"></span>
  <svg width="34" height="34" viewBox="0 0 34 34"><circle cx="13" cy="13" r="10" fill="none" stroke="#d84f2d" stroke-width="4"/><path d="M20 20l10 10" stroke="#d84f2d" stroke-width="6" stroke-linecap="round"/></svg>
</div>

<h2 class="abs h-serif h-day">App of the day</h2>
<h2 class="abs h-serif h-top">Top Apps</h2>
<div class="abs vdiv"></div>

<article class="abs app" style="top:294px">
  <div class="icon" role="img" aria-label="Counting game app icon" style="background:linear-gradient(135deg,#e4892f,#c4321c)"></div>
  <h3>Lorem ipsum dolor</h3>
  <div class="meta">Featured: 46 minutes ago &nbsp;|&nbsp; Rating: 4.50 (1072) Version: 1.0.0 mobile tablet</div>
  <p class="desc">Lorem ipsum dolor sit amet, consectetur adipiscing elit. Nam tincidunt, nulla quis cursus rhoncus, leo est feugiat odio, quis ultricies nibh mauris suscipit purus. Maecenas pharetra feugiat turpis ut lobortis.</p>
  <div class="price paid"><b>$2</b><small>Buy Now</small></div>
  <div class="checks"><i class="hl"></i>Own it<br><i></i>Want it</div>
</article>
<div class="abs hsep" style="top:388px"></div>

<article class="abs app" style="top:414px">
  <div class="icon" role="img" aria-label="Cartoon character app icon" style="background:linear-gradient(135deg,#5a9a3a,#8a4a20)"></div>
  <h3>Lorem ipsum dolor</h3>
  <div class="meta">Featured: 46 minutes ago &nbsp;|&nbsp; Rating: 4.50 (1072) Version: 1.0.0 mobile tablet</div>
  <p class="desc">Lorem ipsum dolor sit amet, consectetur adipiscing elit. Nam tincidunt, nulla quis cursus rhoncus, leo est feugiat odio, quis ultricies nibh mauris suscipit purus. Maecenas pharetra feugiat turpis ut lobortis.</p>
  <div class="price free"><b>Free</b><small>Download</small></div>
  <div class="checks"><i></i>Own it<br><i class="hl"></i>Want it</div>
</article>
<div class="abs hsep" style="top:507px"></div>

<article class="abs app" style="top:533px">
  <div class="icon" role="img" aria-label="Arcade game app icon" style="background:linear-gradient(135deg,#d8332a,#3a7ad0)"></div>
  <h3>Lorem ipsum dolor</h3>
  <div class="meta">Featured: 46 minutes ago &nbsp;|&nbsp; Rating: 4.50 (1072) Version: 1.0.0 mobile tablet</div>
  <p class="desc">Lorem ipsum dolor sit amet, consectetur adipiscing elit. Nam tincidunt, nulla quis cursus rhoncus, leo est feugiat odio, quis ultricies nibh mauris suscipit purus. Maecenas pharetra feugiat turpis ut lobortis.</p>
  <div class="price paid"><b>$2</b><small>Buy Now</small></div>
  <div class="checks"><i class="hl"></i>Own it<br><i></i>Want it</div>
</article>

<aside class="abs topbox">
  <div class="row open" style="top:10px">Lorem ipsum dolor sit amet.
    <div class="sub">Consecture adipiscing elit.<br>Consecture adipiscing elit.<br>Consecture adipiscing elit.<br>Consecture adipiscing elit.</div>
  </div>
  <div class="rule" style="top:84px"></div>
  <div class="row" style="top:93px">Lorem ipsum dolor sit amet.</div>
  <div class="rule" style="top:114px"></div>
  <div class="row" style="top:123px">Lorem ipsum dolor sit amet.</div>
  <div class="rule" style="top:144px"></div>
  <div class="row" style="top:153px">Lorem ipsum dolor sit amet.</div>
  <div class="rule" style="top:174px"></div>
  <div class="row" style="top:184px">Lorem ipsum dolor sit amet.</div>
  <div class="rule" style="top:205px"></div>
  <div class="row" style="top:215px">Lorem ipsum dolor sit amet.</div>
  <div class="rule" style="top:236px"></div>
  <div class="row" style="top:246px">Lorem ipsum dolor sit amet.</div>
  <div class="rule" style="top:267px"></div>
  <div class="row" style="top:276px">Lorem ipsum dolor sit amet.</div>
</aside>
<a class="abs viewmore" href="#">View more</a>

<div class="abs longrule"></div>
<h2 class="abs h-serif h-feat">Featured Apps</h2>
<div class="abs featrule"></div>
<div class="abs arrow" style="left:962px"><svg width="17" height="17"><path d="M10 4.5v8L5 8.5z" fill="#fff"/></svg></div>
<div class="abs arrow" style="left:984px"><svg width="17" height="17"><path d="M7 4.5v8l5-4z" fill="#fff"/></svg></div>

<div class="abs card" style="left:176px">
  <div class="shot" role="img" aria-label="Airline adventure game artwork" style="background:linear-gradient(160deg,#6fa8d8,#2b3f7a)"></div>
  <h4>Lorem ipsum dolor</h4>
  <p>Lorem ipsum dolor amet, cons adipiing elit. Nam tincint, nula quis cursus rhoncus</p>
  <a class="btn" href="#">Download</a>
</div>
<div class="abs cdiv" style="left:376px"></div>
<div class="abs card" style="left:399px">
  <div class="shot" role="img" aria-label="Seaside puzzle game artwork" style="background:linear-gradient(160deg,#7ec0e8,#9a7ec8 55%,#6a9a3a)"></div>
  <h4>Lorem ipsum dolor</h4>
  <p>Lorem ipsum dolor amet, cons adipiing elit. Nam tincint, nula quis cursus rhoncus</p>
  <a class="btn" href="#">Download</a>
</div>
<div class="abs cdiv" style="left:598px"></div>
<div class="abs card" style="left:621px">
  <div class="shot" role="img" aria-label="Truck racing game artwork" style="background:linear-gradient(160deg,#e07a2a,#a82a18)"></div>
  <h4>Lorem ipsum dolor</h4>
  <p>Lorem ipsum dolor amet, cons adipiing elit. Nam tincint, nula quis cursus rhoncus</p>
  <a class="btn" href="#">Download</a>
</div>
<div class="abs cdiv" style="left:823px"></div>
<div class="abs card" style="left:844px">
  <div class="shot" role="img" aria-label="City action game artwork" style="background:linear-gradient(160deg,#c8502a,#e0b040 50%,#7a2a1a)"></div>
  <h4>Lorem ipsum dolor</h4>
  <p>Lorem ipsum dolor amet, cons adipiing elit. Nam tincint, nula quis cursus rhoncus</p>
  <a class="btn" href="#">Download</a>
</div>
<div class="abs endrule"></div>

<footer class="abs footer"></footer>
<nav class="abs fnav"><a href="#">Home</a><span>|</span><a href="#">My Apps</a><span>|</span><a href="#">Reviews</a><span>|</span><a href="#">Blog</a><span>|</span><a href="#">Contact Us</a></nav>
<div class="abs copy">© 2013, BrightPickDigest. | Terms of Use | Privacy Policy</div>
<a class="abs social" href="#" aria-label="Social link 1" style="left:888px"></a>
<a class="abs social" href="#" aria-label="Social link 2" style="left:917px"></a>
<a class="abs social" href="#" aria-label="Social link 3" style="left:947px"></a>
<a class="abs social" href="#" aria-label="Social link 4" style="left:977px"></a>

</body>
</html>
```